A Hair, Beauty and Nails Wholesalers Needs a Business Card Design

We need a business card design for our company which is being passed from parents to daughter, so we wont to re-launch the company with an updated, modern, sophisticated, elegant, chic and fresh look which still incorporates the original colour scheme of Hot Pink, Dark Grey and White. The original logo which is attached can be used on the card but we would like to see some designs with the logo and some without, as we have not yet decided if we want the logo on the card. The name of our company is 'RM's Distributors' and the name of our website is RM's GlowandPolish.example.au. We specialise in supplying a massive range of Hair, Beauty and Nail products to the industry. We are based in QLD, Australia but ship many orders via our website all across Australia.

Industry/Entity Type

Business

```html
<!DOCTYPE html>
<html lang="en">
<head>
<meta charset="utf-8">
<title>RM's Distributors – Business Card</title>
<link rel="stylesheet" href="https://fonts.googleapis.com/css2?family=Lato:wght@400;700&display=swap">
<style>
  :root {
    --hot-pink: #e5097f;
    --pink-deep: #c9076f;
    --charcoal: #1c1c1c;
    --mid-grey: #8f9193;
    --white: #ffffff;
    --backdrop: #e6e6e8;
  }
  * { box-sizing: border-box; margin: 0; padding: 0; }
  html, body {
    width: 1200px; height: 926px; overflow: hidden;
    background: var(--backdrop);
    font-family: "Lato", sans-serif;
  }
  .sheet {
    width: 1200px; height: 926px;
    display: flex; flex-direction: column; align-items: center; justify-content: center;
    gap: 56px;
  }
  .card {
    position: relative; width: 640px; height: 366px; overflow: hidden;
    box-shadow: 0 6px 20px rgba(0,0,0,.18);
  }

  /* ---------- Brand side ---------- */
  .card--brand {
    background: radial-gradient(circle at 40% 30%, var(--hot-pink), var(--pink-deep));
  }
  .brand-mark {
    position: absolute; left: 0; right: 0; top: 92px;
    display: flex; align-items: center; justify-content: center; gap: 16px;
  }
  .brand-mark__dot {
    width: 64px; height: 64px; border-radius: 50%; background: var(--white); flex: none;
  }
  .brand-mark__name {
    color: var(--white); font-weight: 700; font-size: 30px; white-space: nowrap;
  }
  .brand-rule {
    position: absolute; left: 0; right: 0; top: 236px;
    display: flex; align-items: center; gap: 14px;
  }
  .brand-rule::before, .brand-rule::after {
    content: ""; flex: 1; height: 1px; background: rgba(255,255,255,.85);
  }
  .brand-url {
    color: var(--white); font-size: 13px; font-weight: 700; letter-spacing: 3px; white-space: nowrap;
  }

  /* ---------- Contact side ---------- */
  .card--contact { background: var(--white); }
  .card__waves { position: absolute; inset: 0; }
  .contact-person {
    position: absolute; left: 34px; top: 150px; color: var(--white);
  }
  .contact-person__name { font-size: 20px; font-weight: 400; white-space: nowrap; }
  .contact-person__name strong { font-weight: 700; }
  .contact-person__role { font-size: 13px; margin-top: 4px; }
  .contact-list {
    position: absolute; left: 34px; top: 222px; list-style: none;
    color: var(--white); font-size: 14px;
  }
  .contact-list li { display: flex; align-items: center; gap: 8px; height: 22px; white-space: nowrap; }
  .contact-list svg { width: 13px; height: 13px; fill: var(--white); flex: none; }
  .logo-mark {
    position: absolute; right: 30px; top: 58px;
    display: flex; align-items: center; gap: 10px;
  }
  .logo-mark__dot {
    width: 36px; height: 36px; border-radius: 50%; background: var(--hot-pink); flex: none;
  }
  .logo-mark__name {
    color: var(--hot-pink); font-size: 17px; font-weight: 700; white-space: nowrap;
  }
  .company-name {
    position: absolute; left: 378px; top: 170px;
    color: var(--hot-pink); font-size: 23px; font-weight: 700; white-space: nowrap;
  }
</style>
</head>
<body>
<main class="sheet">

  <section class="card card--brand">
    <div class="brand-mark">
      <span class="brand-mark__dot" aria-hidden="true"></span>
      <span class="brand-mark__name">RM's GlowandPolish</span>
    </div>
    <div class="brand-rule"><span class="brand-url">WWW.GLOWANDPOLISH.EXAMPLE.AU</span></div>
  </section>

  <section class="card card--contact">
    <svg class="card__waves" viewBox="0 0 640 366" preserveAspectRatio="none" aria-hidden="true">
      <path fill="var(--hot-pink)" d="M0,0 H150 C240,40 250,205 370,255 C460,292 560,300 640,298 V366 H0 Z"/>
      <path fill="var(--mid-grey)" d="M330,250 C430,300 540,300 640,262 V292 C540,322 420,312 330,250 Z"/>
      <path fill="var(--charcoal)" d="M140,0 C255,28 272,190 385,236 C470,270 560,274 612,262 C560,288 465,288 370,258 C250,214 232,50 140,0 Z"/>
    </svg>

    <div class="contact-person">
      <div class="contact-person__name"><strong>Danielle</strong> Hartley</div>
      <div class="contact-person__role">manager</div>
    </div>

    <ul class="contact-list">
      <li><svg viewBox="0 0 16 16"><path d="M3.6 1.2l2.3 2.6-1.2 1.8c.9 2 2.6 3.7 4.6 4.6l1.8-1.2 2.6 2.3-1.4 2.5C6.6 14 2 9.4 1.2 2.6z"/></svg>(07) 5550 0123</li>
      <li><svg viewBox="0 0 16 16"><path d="M1 3h14v1.2L8 9 1 4.2zM1 5.6l7 4.8 7-4.8V13H1z"/></svg>admin@glowandpolish.example.au</li>
      <li><svg viewBox="0 0 16 16"><path d="M8 0a5 5 0 0 1 5 5c0 4-5 11-5 11S3 9 3 5a5 5 0 0 1 5-5zm0 3a2 2 0 1 0 0 4 2 2 0 0 0 0-4z"/></svg>58 Sample Street, BRIARWOOD, QLD, 4999</li>
    </ul>

    <div class="logo-mark">
      <span class="logo-mark__dot" aria-hidden="true"></span>
      <span class="logo-mark__name">RM's GlowandPolish</span>
    </div>
    <div class="company-name">RM's Distributors</div>
  </section>

</main>
</body>
</html>
```